maple crest homeworks KOVA

Looking for business card design that represents our company. we are maple crest homeworks and we dedicate our skills of home energy efficiency to our customer by providing energy solution to their energy problems.
HVAC
SOLAR
INSULLATION
LIGHTING
DUCT TESTING
KOVA RATING.

```html
<!DOCTYPE html>
<html lang="en">
<head>
<meta charset="utf-8">
<title>Maple Crest Homeworks – Business Card</title>
<link rel="stylesheet" href="https://fonts.googleapis.com/css2?family=Open+Sans:wght@400;600&display=swap">
<style>
  :root {
    --page-bg: #3a3b37;
    --card-bg: #161616;
    --accent-green: #7dc242;
    --text-white: #f2f2f2;
  }
  * { margin: 0; padding: 0; box-sizing: border-box; }
  html, body {
    width: 1200px; height: 824px; overflow: hidden;
    background: var(--page-bg);
    font-family: "Open Sans", Arial, sans-serif;
  }
  .card-row {
    position: absolute; top: 257px; left: 40px;
    display: flex; gap: 40px;
  }
  .card {
    position: relative; width: 540px; height: 309px;
    background: var(--card-bg);
    border-radius: 4px;
    box-shadow: 0 10px 30px rgba(0,0,0,0.45);
    overflow: hidden;
  }
  .accent-bar {
    position: absolute; left: 0; top: 36px;
    width: 16px; height: 88px; background: var(--accent-green);
  }
  .service-list {
    position: absolute; left: 44px; top: 34px;
    list-style: none; color: var(--accent-green);
    font-size: 12px; line-height: 21px; text-transform: uppercase;
    letter-spacing: 0.3px;
  }
  .service-list li::before { content: "• "; }
  .brand-frame {
    position: absolute;
    border: 1.5px solid var(--accent-green); border-radius: 8px;
    display: flex; align-items: center; justify-content: center; gap: 10px;
  }
  .card-front .brand-frame { left: 210px; top: 128px; width: 270px; height: 84px; }
  .card-back .brand-frame { left: 34px; top: 112px; width: 210px; height: 72px; }
  .brand-dot {
    width: 18px; height: 18px; border-radius: 50%;
    background: var(--accent-green); flex: none;
  }
  .brand-name {
    color: var(--accent-green); font-weight: 600;
    text-transform: uppercase; line-height: 1.15; letter-spacing: 0.5px;
  }
  .card-front .brand-name { font-size: 17px; }
  .card-back .brand-name { font-size: 13px; }
  .divider {
    position: absolute; left: 272px; top: 70px;
    width: 1.5px; height: 160px; background: var(--accent-green);
  }
  .contact-block { position: absolute; left: 300px; top: 86px; }
  .person-name { color: var(--text-white); font-size: 26px; font-weight: 400; line-height: 1.1; }
  .job-title {
    color: var(--accent-green); font-size: 13px; font-weight: 600;
    letter-spacing: 1.5px; margin-bottom: 16px;
  }
  .contact-list { list-style: none; }
  .contact-list li {
    display: flex; align-items: center; gap: 10px;
    color: var(--text-white); font-size: 14px; line-height: 28px;
  }
  .contact-icon { width: 16px; height: 16px; fill: var(--accent-green); flex: none; }
</style>
</head>
<body>
<main class="card-row">
  <section class="card card-front">
    <div class="accent-bar"></div>
    <ul class="service-list">
      <li>HVAC</li>
      <li>Solar</li>
      <li>Insullation</li>
      <li>Lighting</li>
      <li>Duct testing</li>
      <li>KOVA rating.</li>
    </ul>
    <div class="brand-frame">
      <span class="brand-dot"></span>
      <span class="brand-name">Maple Crest<br>Homeworks</span>
    </div>
  </section>

  <section class="card card-back">
    <div class="brand-frame">
      <span class="brand-dot"></span>
      <span class="brand-name">Maple Crest<br>Homeworks</span>
    </div>
    <div class="divider"></div>
    <div class="contact-block">
      <h1 class="person-name">Your Name</h1>
      <p class="job-title">JOB TITLE</p>
      <ul class="contact-list">
        <li>
          <svg class="contact-icon" viewBox="0 0 16 16" aria-hidden="true"><path d="M2 5c0-2 12-2 12 0v1h-3V5H5v1H2z"/><path d="M4 7h8l2 6H2z"/><circle cx="8" cy="10" r="1.5" fill="#161616"/></svg>
          000 000 0000
        </li>
        <li>
          <svg class="contact-icon" viewBox="0 0 16 16" aria-hidden="true"><path d="M1 3h14v10H1z"/><path d="M1 3l7 6 7-6" fill="none" stroke="#161616" stroke-width="1.4"/></svg>
          yourname@maplecrest.com
        </li>
        <li>
          <svg class="contact-icon" viewBox="0 0 16 16" aria-hidden="true"><path d="M8 1a5 5 0 0 1 5 5c0 4-5 9-5 9S3 10 3 6a5 5 0 0 1 5-5z"/><circle cx="8" cy="6" r="1.8" fill="#161616"/></svg>
          Your Address
        </li>
      </ul>
    </div>
  </section>
</main>
</body>
</html>
```